integrative health clinic-Medical massage, acupuncture, chiropractic

we like our logo, but are open to new ideas. We need a new card design. We have added chiropractic and acupuncture that we have put under the name of the business. We are an integrative medical clinic

Target Market(s)

General public, athletes

Contact Information for Business Card

Phone 5055583927
Fax 5055583926
Hours Monday-Friday 9-6
Saturday 10-6
The 20% can be smaller on the back

Colors
3176b5
0355a3

Requirements
Must have
• Logo but am open to ideas
Nice to have
• We are an integrated medical clinic but also want to be personable. We want the card fun and inviting

```html
<!DOCTYPE html>
<html lang="en">
<head>
<meta charset="utf-8">
<title>Full Motion Wellness – Business Card</title>
<link rel="stylesheet" href="https://fonts.googleapis.com/css2?family=Roboto:wght@400;500;700&display=swap">
<style>
  :root {
    --brand-blue: #0355a3;
    --brand-light: #3176b5;
    --charcoal: #333333;
    --ink: #111111;
    --paper: #ffffff;
    --rule-grey: #9a9a9a;
  }
  * { box-sizing: border-box; margin: 0; padding: 0; }
  html, body { width: 1200px; height: 960px; overflow: hidden; }
  body {
    background: var(--brand-blue);
    font-family: "Roboto", Arial, sans-serif;
    position: relative;
  }
  .card {
    position: absolute;
    left: 285px;
    width: 630px;
    height: 360px;
    background: var(--paper);
    overflow: hidden;
    box-shadow: 0 14px 24px rgba(0, 0, 0, 0.35);
  }
  .card--front { top: 97px; }
  .card--back { top: 531px; }
  .card__shapes { position: absolute; inset: 0; width: 630px; height: 360px; }

  .brand { position: absolute; left: 22px; display: flex; flex-direction: column; }
  .brand__name { font-weight: 500; color: var(--ink); letter-spacing: -0.5px; white-space: nowrap; }
  .brand__line { display: flex; align-items: center; }
  .brand__dot { border-radius: 50%; background: var(--brand-blue); flex: none; }
  .brand__tagline { color: var(--ink); white-space: nowrap; }

  .card--front .brand { top: 20px; }
  .card--front .brand__name { font-size: 31px; line-height: 36px; }
  .card--front .brand__line { margin-top: 3px; gap: 10px; padding-left: 6px; }
  .card--front .brand__dot { width: 18px; height: 18px; }
  .card--front .brand__tagline { font-size: 13px; }

  .specialties {
    position: absolute; right: 23px; top: 27px;
    text-align: right; color: var(--brand-blue);
    font-size: 20px; line-height: 25px; font-weight: 500;
  }
  .contact { position: absolute; left: 322px; top: 134px; }
  .contact__spine {
    position: absolute; left: 15px; top: 20px; width: 3px; height: 120px;
    background: var(--brand-blue);
  }
  .contact__item { position: absolute; left: 0; display: flex; align-items: center; }
  .contact__icon {
    width: 32px; height: 32px; border-radius: 50%;
    background: var(--brand-blue); display: flex; align-items: center; justify-content: center;
  }
  .contact__text {
    position: absolute; left: 55px; width: 240px;
    font-size: 13.6px; line-height: 18px; color: var(--ink); white-space: nowrap;
  }
  .contact__item--address { top: 4px; }
  .contact__item--address .contact__text { top: -1px; }
  .contact__item--phone { top: 65px; }
  .contact__item--phone .contact__text { top: -1px; }
  .contact__item--web { top: 125px; }
  .contact__item--web .contact__text { top: -3px; left: 57px; line-height: 20px; }
  .contact__rule {
    position: absolute; left: 57px; width: 81px; height: 1px; background: var(--rule-grey);
  }
  .contact__rule::before {
    content: ""; position: absolute; left: 0; top: -1px; width: 25px; height: 2px; background: var(--brand-blue);
  }
  .contact__rule--one { top: 58px; }
  .contact__rule--two { top: 118px; }

  .hours {
    position: absolute; left: 329px; top: 324px;
    display: flex; align-items: center; gap: 31px;
    color: var(--paper); font-size: 14.5px;
  }

  .card--back .brand { top: 24px; }
  .card--back .brand__name { font-size: 56px; line-height: 62px; letter-spacing: -1.5px; }
  .card--back .brand__line { margin-top: 4px; gap: 22px; padding-left: 56px; }
  .card--back .brand__dot { width: 40px; height: 40px; }
  .card--back .brand__tagline { font-size: 24px; }

  .offer {
    position: absolute; left: 0; right: 0; top: 162px;
    text-align: center; color: var(--brand-blue);
    font-size: 36px; font-weight: 700; letter-spacing: 0.2px;
  }
  .booking {
    position: absolute; right: 23px; top: 250px;
    text-align: right; color: var(--brand-blue);
    font-size: 20px; line-height: 26px; font-weight: 500;
  }
  .coverage {
    position: absolute; right: 23px; top: 314px;
    color: var(--paper); font-size: 14.4px; white-space: nowrap;
  }
</style>
</head>
<body>

  <section class="card card--front">
    <svg class="card__shapes" viewBox="0 0 788 450" aria-hidden="true">
      <rect x="178" y="390" width="610" height="60" fill="var(--brand-blue)"/>
      <polygon points="0,224 178,390 178,450 0,450" fill="var(--brand-blue)"/>
      <polygon points="0,258 206,450 0,450" fill="var(--brand-light)"/>
      <polygon points="0,276 186,450 0,450" fill="var(--brand-blue)"/>
      <polygon points="0,284 178,450 0,450" fill="var(--charcoal)"/>
    </svg>

    <div class="brand">
      <span class="brand__name">Full Motion Wellness</span>
      <div class="brand__line">
        <span class="brand__dot"></span>
        <span class="brand__tagline">Sports Therapy and Wellness Center</span>
      </div>
    </div>

    <p class="specialties">Specializing in Medical,<br>Sports Massage and<br>Manual Therapies</p>

    <div class="contact">
      <span class="contact__spine"></span>
      <div class="contact__item contact__item--address">
        <span class="contact__icon">
          <svg width="16" height="18" viewBox="0 0 16 18" aria-hidden="true"><path d="M8 1a5.5 5.5 0 0 0-5.5 5.5C2.5 11 8 17 8 17s5.5-6 5.5-10.5A5.5 5.5 0 0 0 8 1z" fill="none" stroke="#fff" stroke-width="1.8"/><circle cx="8" cy="6.5" r="2" fill="#fff"/></svg>
        </span>
        <p class="contact__text">418 Cedar Run St,<br>B4 Santa Fe, NM 87501</p>
      </div>
      <span class="contact__rule contact__rule--one"></span>
      <div class="contact__item contact__item--phone">
        <span class="contact__icon">
          <svg width="18" height="14" viewBox="0 0 18 14" aria-hidden="true"><path d="M1 5c0-2 3.5-3.5 8-3.5S17 3 17 5v1.5h-3.5V4.5h-9v2H1z" fill="#fff"/><path d="M3.5 7.5h11l1.5 5.5H2z" fill="#fff"/><circle cx="9" cy="10" r="1.6" fill="var(--brand-blue)"/></svg>
        </span>
        <p class="contact__text">Phone: 5055583927<br>Fax: 5055583926</p>
      </div>
      <span class="contact__rule contact__rule--two"></span>
      <div class="contact__item contact__item--web">
        <span class="contact__icon">
          <svg width="16" height="16" viewBox="0 0 16 16" aria-hidden="true"><g fill="none" stroke="#fff" stroke-width="1.8" stroke-linecap="round"><path d="M6.5 9.5l3-3"/><path d="M7.5 4.5l1.2-1.2a2.6 2.6 0 0 1 3.7 3.7l-1.2 1.2"/><path d="M8.5 11.5l-1.2 1.2a2.6 2.6 0 0 1-3.7-3.7l1.2-1.2"/></g></svg>
        </span>
        <p class="contact__text">www.fullmotionwellnessnm.com<br>info@fullmotionwellnessnm.com</p>
      </div>
    </div>

    <div class="hours">
      <svg width="18" height="17" viewBox="0 0 18 17" aria-hidden="true"><g fill="none" stroke="#fff" stroke-width="1.2"><rect x="1" y="2.5" width="14" height="12" rx="1"/><path d="M1 5.5h14M4.5 1v3M11.5 1v3"/><circle cx="13.5" cy="13" r="3" fill="var(--brand-blue)"/><path d="M13.5 11.5v1.6h1.2"/></g></svg>
      <span>Monday-Friday 9-6, Saturday 10-6</span>
    </div>
  </section>

  <section class="card card--back">
    <svg class="card__shapes" viewBox="0 0 788 450" aria-hidden="true">
      <rect x="178" y="390" width="610" height="60" fill="var(--brand-blue)"/>
      <polygon points="0,224 178,390 178,450 0,450" fill="var(--brand-blue)"/>
      <polygon points="0,258 206,450 0,450" fill="var(--brand-light)"/>
      <polygon points="0,276 186,450 0,450" fill="var(--brand-blue)"/>
      <polygon points="0,284 178,450 0,450" fill="var(--charcoal)"/>
      <polygon points="609,0 788,0 788,168" fill="var(--brand-blue)"/>
      <polygon points="636,0 788,0 788,142" fill="var(--brand-light)"/>
      <polygon points="654,0 788,0 788,126" fill="var(--brand-blue)"/>
      <polygon points="666,0 788,0 788,116" fill="var(--charcoal)"/>
    </svg>

    <div class="brand">
      <span class="brand__name">Full Motion Wellness</span>
      <div class="brand__line">
        <span class="brand__dot"></span>
        <span class="brand__tagline">Sports Therapy and Wellness Center</span>
      </div>
    </div>

    <p class="offer">20% OFF FIRST VISIT</p>

    <p class="booking">Book Online<br>www.fullmotionwellnessnm.com</p>

    <p class="coverage">We accept some insurances, Worker's Comp and Personal Injury</p>
  </section>

</body>
</html>
```